M Zyvantics Buisness Cards

I need a technology focused clean business card for my employees. I have attached out logo to include in the mocks. We're a modern tech consulting firm that drives to interface humanity with technology in a truly cohesive fashion.

```html
<!DOCTYPE html>
<html lang="en">
<head>
<meta charset="utf-8">
<title>M Zyvantics Business Cards</title>
<link href="https://fonts.googleapis.com/css2?family=Roboto:wght@400;700&display=swap" rel="stylesheet">
<style>
  :root {
    --stage: #2b2b2b;
    --card: #f7f7f7;
    --brand-blue: #1f73be;
    --brand-navy: #1d4f91;
    --text-grey: #6b6b6b;
    --mark-grey: #8a8a8a;
  }
  * { box-sizing: border-box; margin: 0; padding: 0; }
  html, body {
    width: 1200px; height: 997px; overflow: hidden;
    background: var(--stage);
    font-family: "Roboto", Arial, sans-serif;
  }
  .stage { position: relative; width: 1200px; height: 997px; }

  .card {
    position: absolute;
    width: 520px; height: 298px;
    background: var(--card);
    border-radius: 16px;
    overflow: hidden;
  }

  /* Front */
  .card-front { left: 90px; top: 130px; }
  .front-wordmark {
    position: absolute; inset: 0;
    display: flex; align-items: center; justify-content: center; gap: 16px;
  }
  .front-wordmark .dot {
    width: 44px; height: 44px; border-radius: 50%;
    background: var(--brand-blue);
  }
  .front-wordmark .name {
    font-size: 48px; font-weight: 700; color: var(--mark-grey);
    letter-spacing: 1px;
  }

  /* Back */
  .card-back { left: 590px; top: 520px; }
  .back-badge {
    position: absolute; left: 34px; top: 0;
    width: 130px; height: 130px;
    background: var(--brand-blue);
    display: flex; align-items: center; justify-content: center;
  }
  .back-badge .name {
    color: #fff; font-weight: 700; font-size: 17px;
  }
  .holder { position: absolute; left: 40px; top: 148px; }
  .holder-name {
    font-size: 22px; font-weight: 700; color: var(--brand-navy); letter-spacing: .5px;
  }
  .holder-title {
    font-size: 15px; font-weight: 700; color: var(--text-grey); margin-top: 2px;
  }
  .contact-list { list-style: none; margin-top: 10px; }
  .contact-list li {
    display: flex; align-items: center; gap: 10px;
    font-size: 16px; color: var(--text-grey); line-height: 24px;
  }
  .contact-icon { width: 14px; height: 14px; flex: none; }
  .website {
    position: absolute; right: 34px; top: 218px;
    font-size: 17px; font-weight: 700; color: var(--brand-navy); letter-spacing: .5px;
  }
  .bottom-band {
    position: absolute; left: 0; right: 0; bottom: 0; height: 12px;
    background: var(--brand-blue);
  }
</style>
</head>
<body>
<main class="stage">

  <section class="card card-front" aria-label="Card front">
    <div class="front-wordmark">
      <span class="dot"></span>
      <span class="name">M Zyvantics</span>
    </div>
  </section>

  <section class="card card-back" aria-label="Card back">
    <div class="back-badge"><span class="name">M Zyvantics</span></div>

    <div class="holder">
      <p class="holder-name">DANA CORVEL</p>
      <p class="holder-title">Director</p>
      <ul class="contact-list">
        <li>
          <svg class="contact-icon" viewBox="0 0 14 14" aria-hidden="true">
            <circle cx="7" cy="7" r="7" fill="var(--brand-blue)"/>
            <path d="M4 4.5c0 3 2.5 5.5 5.5 5.5l.8-1.2-1.5-.9-.7.6c-.9-.4-1.7-1.2-2.1-2.1l.6-.7-.9-1.5z" fill="#fff"/>
          </svg>
          555.014.2290
        </li>
        <li>
          <svg class="contact-icon" viewBox="0 0 14 14" aria-hidden="true">
            <circle cx="7" cy="7" r="7" fill="var(--brand-blue)"/>
            <rect x="4.5" y="3" width="5" height="8" rx="1" fill="#fff"/>
          </svg>
          555.016.7731
        </li>
        <li>
          <svg class="contact-icon" viewBox="0 0 14 14" aria-hidden="true">
            <circle cx="7" cy="7" r="7" fill="var(--brand-blue)"/>
            <rect x="3.5" y="4.5" width="7" height="5" fill="#fff"/>
            <path d="M3.5 4.5 7 7.3l3.5-2.8" stroke="var(--brand-blue)" stroke-width=".8" fill="none"/>
          </svg>
          dana@zyvantics.com
        </li>
      </ul>
    </div>

    <p class="website">www.zyvantics.com</p>
    <div class="bottom-band"></div>
  </section>

</main>
</body>
</html>
```